Book: The Seasoned Steward - Good Living IS NOT a Bystander Game

This book is about taking action, and being involved in making health decisions. The title of the book tells two things. First, this book helps people control their health outcomes better. Secondly, that you cannot get great results by just letting doctors make decisions for you (as a spectator). A cover could either show (1) An empowered patient who is "examining" or "influencing" their health outcomes, OR (2) A passive patient watching what is happening. It can be abstract.

All this is for the back of the book: You have been led to believe that two things count when it comes to outcomes: the skills of our practitioners and the effectiveness of the treatments they provide. You don’t even factor yourself into the equation! But you certainly should. You would not want a mediocre doctor, so why be a so-so patient or a passive healthcare consumer? The more evolved and involved you are as a patient and consumer, the closer your healthcare will come to match your needs and your goals. The archetypical relationship we have with healthcare providers needs to be kicked to the curb; it is not in your best interests. You are often being shortchanged, and I intend to let you know why. Reviews This book makes you reflect on your health further and helps you “invest in prevention". It makes you bolder and more conscious of how to navigate the healthcare system. All in all, The Seasoned Steward is an eye-opener. Miriam Oswick, Certified Nutritionist Practitioner It pays to be informed and proactive with our health. If your goal is to become a smarter healthcare consumer and be more actively involved in your personal wellness, then The Seasoned Steward is required reading. Offering practical tips, principles and guidelines, this book is an important, straightforward resource to navigating the path of self-advocacy. Lorena Pavitt, Wellness Coach Once again, Dr. Imogen uses her experience, knowledge and research to give us the tools to take charge of our health. This is a gift. Imogen is an incredible researcher and brings forward a very balanced approach in her writings. Dr. Wendy Pruitt DDS. MBA The seasoned steward is “expertly” written. Dr. Haverly poses some thought-provoking questions that encourage one to change how they approach their health and retain some of the ‘power’ they have in influencing their own health and outcomes. Eleni Roula Papadimas BSc. Clinical Biologist, Consultant of Oncology unit, Kyrtos Hospital, Athens, Greece. Very interesting read! The book is written for You. It is very personable and relatable. Tons of useful and innovative information. Dr. Nino Gvelesiani, DDS About the author Dr. Imogen Haverly is an accomplished naturopathic doctor, author, blogger and speaker. She previously authored Canada’s most comprehensive book on food labels to date, The Savvy Pantry Keeper: A Primer on Grocery Tags and Tales. Her personal healing journey and triumph with fibromyalgia inspired her to become a relentless advocate for taking health into our own hands. This book is a continuation of that passion. Dr. Imogen, as @TheLectureMedic, dedicates much of her time teaching others how to think about their health.

Target Market(s)

Healthcare consumers. Ordinary people.

Industry/Entity Type

Health And Wellness

Font styles to use
Sans Serif
Other font styles liked:
• Simple and elegant

Colors
89d0c7
34a6d7

Requirements
Must have
• This book will be published
1) E-book in JPEG, PNG, TIFF
2) Printed book cover: 5.25"x8" (13.335x20.32 cm) (38,792 words)... pages about 160??? - provide in word file as well so I can edit
Image must be 2400X1600 pixels
3) Display of 3D book for advertisements
Nice to have
• *copy the design layout for my last book (BACK COVER) - attached
*attaching an example of an image from istock that is an EXAMPLE of a creative way to showing a patient being a SPECTATOR. I made a cover using it: https://www.pictovault-example.com/fr/vectoriel/calme-du-corps-gm908172635-71029384
*Nice elegant font (like in my example attached)
Should not have
• *avoid clipart of doctors or doctors with patients... this is too general

```html
<!DOCTYPE html>
<html lang="en">
<head>
<meta charset="utf-8">
<title>The Seasoned Steward – Front Cover</title>
<link href="https://fonts.googleapis.com/css2?family=Jost:ital,wght@0,300;0,400;1,400&display=swap" rel="stylesheet">
<style>
  :root {
    --backdrop: #cfe5e5;
    --cover-white: #ffffff;
    --band-blue: #9ccbd8;
    --ink: #2a2a2a;
    --title-white: #ffffff;
    --art-blue: #5fa4c4;
    --art-rust: #cf8a68;
    --art-gold: #e3c15e;
    --art-green: #86bc82;
  }
  * { margin: 0; padding: 0; box-sizing: border-box; }
  html, body {
    width: 1200px;
    height: 1200px;
    overflow: hidden;
    background: var(--backdrop);
  }
  .book-cover {
    position: absolute;
    left: 240px;
    top: 51px;
    width: 720px;
    height: 1098px;
    background: var(--cover-white);
    font-family: "Jost", sans-serif;
    box-shadow: 0 6px 24px rgba(40, 80, 90, 0.18);
    overflow: hidden;
  }
  .tangle-art {
    position: absolute;
    left: 150px;
    top: 36px;
    width: 440px;
    height: 280px;
  }
  .title-band {
    position: absolute;
    left: 0;
    top: 330px;
    width: 100%;
    height: 300px;
    background: var(--band-blue);
    padding: 24px 0 0 52px;
  }
  .book-title {
    color: var(--title-white);
    font-weight: 300;
    font-size: 100px;
    line-height: 0.98;
    letter-spacing: 1px;
  }
  .book-subtitle {
    margin-top: 22px;
    color: var(--ink);
    font-style: italic;
    font-weight: 400;
    font-size: 31px;
    letter-spacing: 1px;
  }
  .character-art {
    position: absolute;
    left: 50px;
    top: 650px;
    width: 620px;
    height: 290px;
  }
  .author-block {
    position: absolute;
    right: 40px;
    bottom: 46px;
    color: var(--ink);
  }
  .author-name {
    font-weight: 400;
    font-size: 33px;
    letter-spacing: 1px;
  }
  .author-credential {
    font-weight: 400;
    font-size: 20px;
    letter-spacing: 3px;
    margin-top: 2px;
  }
</style>
</head>
<body>
  <main class="book-cover">
    <svg class="tangle-art" viewBox="0 0 440 280" role="img" aria-label="Illustration of a tangled knot of blue, rust, gold and green lines">
      <defs>
        <linearGradient id="tangle-tone" x1="0" y1="0" x2="1" y2="1">
          <stop offset="0%" stop-color="#cf8a68" stop-opacity="0.55"/>
          <stop offset="35%" stop-color="#5fa4c4" stop-opacity="0.6"/>
          <stop offset="65%" stop-color="#e3c15e" stop-opacity="0.6"/>
          <stop offset="100%" stop-color="#86bc82" stop-opacity="0.55"/>
        </linearGradient>
      </defs>
      <rect width="440" height="280" rx="120" fill="url(#tangle-tone)"/>
    </svg>

    <section class="title-band">
      <h1 class="book-title">The Seasoned<br>Steward</h1>
      <p class="book-subtitle">Good Living isn't a Bystander Game</p>
    </section>

    <svg class="character-art" viewBox="0 0 620 290" role="img" aria-label="Illustration of four coloured characters in green, blue, rust and gold, joined by lines to the knot above">
      <defs>
        <linearGradient id="character-tone" x1="0" y1="0" x2="1" y2="0">
          <stop offset="0%" stop-color="#86bc82" stop-opacity="0.75"/>
          <stop offset="33%" stop-color="#5fa4c4" stop-opacity="0.75"/>
          <stop offset="66%" stop-color="#cf8a68" stop-opacity="0.75"/>
          <stop offset="100%" stop-color="#e3c15e" stop-opacity="0.75"/>
        </linearGradient>
      </defs>
      <rect width="620" height="290" rx="28" fill="url(#character-tone)"/>
    </svg>

    <footer class="author-block">
      <p class="author-name">Dr. Imogen Haverly, ND, MA</p>
      <p class="author-credential">Doctor of Naturopathic Medicine</p>
    </footer>
  </main>
</body>
</html>
```